HollowPine Ventures Inc. Business Card Design

My business is custom renovations and homes.I would need to have a new business logo created to go along with my company name. The business card should be of a modern style as this is the market I am focused on. I would need my contact information and website posted on the card. I would also like to list a few of the tasks I conduct on the card (such as: Renovations, Additions, Repairs, New Homes, Design, Consultations). On the reverse of the card I currently have just my logo and my motto, "Shaping A Bold Path". However, I am open to completely changing everything as I am starting a new year and would like to excel further. Any new ideas and suggestions are always welcomed. Thank you.

Target Market(s)

Upscale residential and commercial renovations and builds

Industry/Entity Type

Business

Contact Information for Business Card

I would like the design to be able to be laser cut or burnt onto a wooden business card. I will be creating one option of cards for really loyal customers (wooden) and a second option for the everyday customer (paper).

Font styles to use
Other font styles liked:
• Calibri / anything of mordern taste

Colors
f37122
5c5c5c
474747
ffffff

Requirements
Must have
• I would like the colours of my business to be a sharp orange and grey. I believe this will symbolize a modern style. I am open to other suggestions if this is not suitable for the designers tastes. My contact info as follows:
• Will Marsh
• President
• HollowPine Ventures Inc.
• 555-214-3987
• will@hollowpineventures.example
• I would like my website (currently under construction) hollowpineventures.example on the card aswell.
Nice to have
• Along with a modern logo representing HollowPine, I would like something on the card besides the logo and contact information. Perhaps a small background design. I feel it may be nice to have my services listed on the card (in smaller font on the bottom) Renovations, Additions, Repairs, Design, Consultations.
Should not have
• The business card should not have too many different colors. Should not have rounded corners.

```html
<!DOCTYPE html>
<html lang="en">
<head>
<meta charset="utf-8">
<title>HollowPine Ventures Inc. – Business Card</title>
<link href="https://fonts.googleapis.com/css2?family=Open+Sans:wght@400;600;700&display=swap" rel="stylesheet">
<style>
  :root {
    --orange: #f37122;
    --orange-faint: #fbe1cf;
    --grey: #5c5c5c;
    --grey-dark: #474747;
    --white: #ffffff;
    --backdrop: #e6e6e6;
  }
  * { box-sizing: border-box; margin: 0; padding: 0; }
  html, body { width: 1189px; height: 1200px; overflow: hidden; }
  body {
    background: var(--backdrop);
    font-family: "Open Sans", Arial, sans-serif;
    color: var(--grey-dark);
    position: relative;
  }
  .card {
    position: absolute;
    left: 191px;
    width: 807px;
    height: 460px;
    background: var(--white);
    box-shadow: 0 6px 14px rgba(0,0,0,0.28);
    overflow: hidden;
  }
  .card--front { top: 111px; }
  .card--back { top: 620px; }

  /* Front */
  .front__decor {
    position: absolute;
    left: 0; top: 55px;
    width: 408px; height: 355px;
    background: var(--orange-faint);
  }
  .front__brand {
    position: absolute;
    right: 32px; top: 300px;
    display: flex; flex-direction: column; align-items: flex-end; gap: 18px;
  }
  .brand__mark {
    width: 78px; height: 78px;
    background: var(--orange);
  }
  .brand__name {
    font-weight: 700;
    font-size: 20px;
    color: var(--orange);
    white-space: nowrap;
  }

  /* Back */
  .back__brand {
    position: absolute;
    left: 40px; width: 320px; top: 118px;
    display: flex; flex-direction: column; align-items: center; gap: 26px;
  }
  .back__brand .brand__mark { width: 140px; height: 140px; }
  .back__brand .brand__name { font-size: 20px; }
  .back__divider {
    position: absolute;
    left: 386px; top: 53px;
    width: 2px; height: 331px;
    background: var(--grey-dark);
  }
  .person { position: absolute; left: 432px; top: 78px; }
  .person__name {
    font-weight: 600; font-size: 31px; line-height: 1.1;
    color: var(--grey-dark);
  }
  .person__title {
    font-size: 21px; line-height: 1.25;
    color: var(--orange);
  }
  .contacts {
    position: absolute; left: 430px; top: 260px;
    list-style: none;
  }
  .contacts li {
    display: flex; align-items: center; gap: 19px;
    font-size: 19px; color: var(--grey-dark);
    height: 27px; margin-bottom: 9px;
  }
  .contacts svg { width: 19px; height: 19px; flex: none; }
  .services {
    position: absolute; left: 0; right: 0; top: 405px;
    text-align: center;
    font-size: 17px; font-weight: 600; letter-spacing: 1.3px;
    color: var(--grey-dark);
    word-spacing: 2px;
  }
</style>
</head>
<body>
  <section class="card card--front" aria-label="Card front">
    <div class="front__decor" aria-hidden="true"></div>
    <div class="front__brand">
      <div class="brand__mark" aria-hidden="true"></div>
      <div class="brand__name">HollowPine Ventures Inc.</div>
    </div>
  </section>

  <section class="card card--back" aria-label="Card back">
    <div class="back__brand">
      <div class="brand__mark" aria-hidden="true"></div>
      <div class="brand__name">HollowPine Ventures Inc.</div>
    </div>
    <div class="back__divider" aria-hidden="true"></div>
    <div class="person">
      <div class="person__name">Will Marsh</div>
      <div class="person__title">President</div>
    </div>
    <ul class="contacts">
      <li>
        <svg viewBox="0 0 20 20" aria-hidden="true"><rect width="20" height="20" fill="#f37122"/><path d="M6 4c1 0 2 2.5 2 3s-1 1-1 1.5c0 1 3 4.5 4 4.5.5 0 1-1 1.5-1s3 1 3 2-1.5 2-2.5 2C8 16 4 11 4 7c0-1.5 1-3 2-3z" fill="#fff"/></svg>
        <span>555-214-3987</span>
      </li>
      <li>
        <svg viewBox="0 0 20 20" aria-hidden="true"><rect width="20" height="20" fill="#f37122"/><rect x="4" y="6" width="12" height="8" fill="none" stroke="#fff" stroke-width="1.4"/><path d="M4 6l6 5 6-5" fill="none" stroke="#fff" stroke-width="1.4"/></svg>
        <span>will@hollowpineventures.example</span>
      </li>
      <li>
        <svg viewBox="0 0 20 20" aria-hidden="true"><rect width="20" height="20" fill="#f37122"/><circle cx="10" cy="10" r="6" fill="none" stroke="#fff" stroke-width="1.4"/><ellipse cx="10" cy="10" rx="2.5" ry="6" fill="none" stroke="#fff" stroke-width="1.2"/><path d="M4 10h12" stroke="#fff" stroke-width="1.2"/></svg>
        <span>www.hollowpineventures.example</span>
      </li>
    </ul>
    <p class="services">Renovations | Additions | Repairs | New Homes | Consultations</p>
  </section>
</body>
</html>
```